New Business Card Design Project

I need a clean, professional business card. I'd like it to have some color, but not be wild. We do technology consulting and we have clients large and small who trust us with some of their most important data and projects. Simple but not boring should drive all design proposals. Multicolored and two sided, but with a matte finish, I think.
For more on tone, check out our website: http://quorvantis.example

Target Market(s)

Upper management of respected businesses. Tech savvy, but not "hipster".

Industry/Entity Type

Business

Requirements
Must have
• Files need to be provided in .eps and in .pdf in a manner that allows for easy updates.
Must have Name, Title, Phone, Email, Twitter, Website
Nice to have
• Logo/Name shouldn't be too big. One thing I've read several places is that the bigger the logo, the smaller the brand. A good article on dos and don'ts here: http://www.brindlepost.example/2011/02/business-card-experience.html

```html
<!DOCTYPE html>
<html lang="en">
<head>
<meta charset="utf-8">
<title>Quorvantis business card</title>
<link rel="stylesheet" href="https://fonts.googleapis.com/css2?family=Montserrat:wght@400;600&family=Varela+Round&display=swap">
<style>
  :root {
    --teal: #2f8891;
    --teal-deep: #277a83;
    --teal-light: #4ea2aa;
    --ink: #6a6d70;
    --ink-dark: #55585b;
    --paper: #ffffff;
    --stage: #e4e6e7;
  }
  * { box-sizing: border-box; margin: 0; padding: 0; }
  html, body {
    width: 1200px; height: 900px; overflow: hidden;
    background: var(--stage);
  }
  .stage {
    position: relative; width: 1200px; height: 900px;
  }
  .card {
    position: absolute; left: 300px; width: 600px; height: 343px;
    border-radius: 16px; overflow: hidden;
    box-shadow: 0 6px 18px rgba(0,0,0,0.14);
  }
  .card--back { top: 70px; background: var(--teal); }
  .card--front { top: 470px; background: var(--paper); }

  .wordmark {
    font-family: "Montserrat", sans-serif; font-weight: 400;
    letter-spacing: 2px; display: flex; align-items: center; gap: 14px;
  }
  .wordmark__dot { width: 14px; height: 14px; border-radius: 50%; }

  .card--back .wordmark {
    position: absolute; left: 0; right: 0; top: 118px; justify-content: center;
    color: var(--paper); font-size: 44px;
  }
  .card--back .wordmark__dot { background: var(--paper); }

  .card--front .wordmark {
    position: absolute; left: 34px; top: 26px;
    color: var(--ink); font-size: 32px;
  }
  .card--front .wordmark__dot { background: var(--teal); width: 11px; height: 11px; }

  .dot-band {
    position: absolute; left: 0; right: 0; bottom: 0; height: 92px;
  }
  .card--back .dot-band {
    background: linear-gradient(180deg, rgba(255,255,255,0) 0%, rgba(255,255,255,0.28) 100%);
  }
  .card--front .dot-band {
    bottom: 18px; height: 80px;
    background: linear-gradient(180deg, rgba(47,136,145,0.08) 0%, rgba(47,136,145,0.35) 100%);
  }

  .person {
    position: absolute; left: 0; right: 0; top: 100px; text-align: center;
    font-family: "Montserrat", sans-serif;
  }
  .person__name { font-size: 24px; font-weight: 600; letter-spacing: 1.5px; }
  .person__first { color: var(--teal); }
  .person__last { color: var(--ink-dark); }
  .person__title {
    font-family: "Varela Round", sans-serif; color: var(--ink);
    font-size: 15px; letter-spacing: 1px; margin-top: 2px;
  }

  .contact {
    position: absolute; top: 172px;
    font-family: "Varela Round", sans-serif; color: var(--ink); font-size: 16px;
    list-style: none;
  }
  .contact--left { left: 34px; }
  .contact--right { left: 340px; top: 196px; }
  .contact li { display: flex; align-items: center; gap: 9px; height: 24px; white-space: nowrap; }
  .contact svg { width: 16px; height: 16px; flex: none; }
  .icon-fill { fill: var(--teal); }
  .icon-line { fill: none; stroke: var(--teal); stroke-width: 1.6; }
</style>
</head>
<body>
<main class="stage">

  <section class="card card--back" aria-label="Card back">
    <div class="wordmark"><span class="wordmark__dot"></span>QUORVANTIS</div>
    <div class="dot-band" role="img" aria-label="Dotted equalizer pattern in white along the bottom edge"></div>
  </section>

  <section class="card card--front" aria-label="Card front">
    <div class="wordmark"><span class="wordmark__dot"></span>QUORVANTIS</div>

    <div class="person">
      <p class="person__name"><span class="person__first">DANA</span> <span class="person__last">WHITLOCK</span></p>
      <p class="person__title">CEO</p>
    </div>

    <ul class="contact contact--left">
      <li>
        <svg viewBox="0 0 16 16" aria-hidden="true"><rect class="icon-line" x="4" y="1" width="8" height="14" rx="1.5"/><circle class="icon-fill" cx="8" cy="12.3" r="0.9"/></svg>
        +1 (555) 014 2290. Ext418
      </li>
      <li>
        <svg viewBox="0 0 16 16" aria-hidden="true"><rect class="icon-fill" x="1" y="3" width="14" height="10" rx="1"/><path d="M1.5 3.5 L8 9 L14.5 3.5" fill="none" stroke="#fff" stroke-width="1.2"/></svg>
        dana@quorvantis.example
      </li>
    </ul>

    <ul class="contact contact--right">
      <li>
        <svg viewBox="0 0 16 16" aria-hidden="true"><circle class="icon-fill" cx="8" cy="8" r="6"/></svg>
        @quorvantist
      </li>
      <li>
        <svg viewBox="0 0 16 16" aria-hidden="true"><circle class="icon-line" cx="8" cy="8" r="6.5"/><ellipse class="icon-line" cx="8" cy="8" rx="2.8" ry="6.5"/><path class="icon-line" d="M1.5 8 H14.5 M2.6 4.6 H13.4 M2.6 11.4 H13.4"/></svg>
        www.quorvantis.example
      </li>
    </ul>

    <div class="dot-band" role="img" aria-label="Dotted equalizer pattern in teal along the bottom edge"></div>
  </section>

</main>
</body>
</html>
```